Cover design for new academic journal on deconstruction and psychoanalysis

We need a cover for a new academic journal on deconstruction and psychoanalysis. The name of the journal is "The Liminal Remainder: A Journal of Deconstruction and Psychoanalysis" (LR) and it is published by the Calloway Ridge University Press(CRP).

Here is a description of the journal on the CRP website:

http://www.callowayridgepress.example.edu/product/The-Liminal-Remainder,482917.aspx

We are looking for a design that is more abstract and does not have icons or photographs of people, especially not photos of Valmont or Kessler. The design should be contemporary with clean lines and simple fonts. Again, it should be abstract, with no icons or iconography.

The cover should simply have the full name of the journal and then "Volume 1, Issue 1, 2014" on the cover and "Vol. 1, No. 1, 2014" on the spine.

Attached you can see some ideas that we rejected from CRP. It is important that you understand that these designs were rejected and are just being offered as examples of what the cover will look like in general, as a template of sorts.

The cover should have a bold abstract design, with a space for the title and "Volume 1, Issue 1, 2014."

Something bold and contemporary.

Academics, scholars and psychoanalysts.

University

Sans Serif

• Must be abstract, bold, have color, and must be contemporary.
• No icons, no photographs of Valmont, Kessler, or anyone.

```html
<!DOCTYPE html>
<html lang="en">
<head>
<meta charset="utf-8">
<title>The Liminal Remainder — Journal Cover</title>
<link rel="stylesheet" href="https://fonts.googleapis.com/css2?family=Arimo:wght@400;700&display=swap">
<style>
  :root {
    --lime: #9fd62a;
    --green: #2fb35a;
    --teal: #1f9d9a;
    --aqua: #3fb6c4;
    --blue: #1f6fa8;
    --deep: #0d2a33;
    --void: #0a1f25;
    --ink-light: #f2f2f2;
    --ink-soft: #e6eef0;
  }
  * { margin: 0; padding: 0; box-sizing: border-box; }
  html, body {
    width: 1200px;
    height: 900px;
    overflow: hidden;
    background: var(--deep);
  }
  .cover {
    position: relative;
    width: 1200px;
    height: 900px;
    overflow: hidden;
    font-family: "Arimo", Arial, sans-serif;
  }
  .cover-art {
    position: absolute;
    inset: 0;
    background:
      radial-gradient(ellipse 170px 300px at 720px 420px, var(--void) 0%, rgba(10,31,37,0.85) 45%, rgba(10,31,37,0) 100%),
      radial-gradient(ellipse 520px 420px at 130px 820px, rgba(200,220,40,0.75) 0%, rgba(200,220,40,0) 70%),
      radial-gradient(ellipse 380px 700px at 80px 300px, rgba(80,200,60,0.7) 0%, rgba(80,200,60,0) 75%),
      linear-gradient(100deg, var(--green) 0%, var(--teal) 35%, var(--aqua) 60%, var(--blue) 100%);
  }
  .spine-title,
  .spine-issue {
    position: absolute;
    color: #ffffff;
    font-weight: 700;
    white-space: nowrap;
    transform-origin: left top;
    transform: rotate(90deg);
  }
  .spine-title {
    left: 614px;
    top: 55px;
    font-size: 25px;
    letter-spacing: 0.5px;
  }
  .spine-issue {
    left: 616px;
    top: 688px;
    font-size: 14px;
    letter-spacing: 1px;
  }
  .front-title {
    position: absolute;
    left: 692px;
    top: 205px;
    color: var(--ink-light);
    font-weight: 700;
    font-size: 70px;
    line-height: 84px;
    letter-spacing: 9px;
    text-shadow: 2px 3px 2px rgba(0,0,0,0.45);
  }
  .front-title span { display: block; }
  .front-subtitle {
    position: absolute;
    left: 692px;
    top: 576px;
    color: var(--ink-soft);
    font-size: 20px;
    line-height: 56px;
    letter-spacing: 2.2px;
  }
  .front-subtitle span { display: block; }
  .front-issue {
    position: absolute;
    left: 692px;
    top: 795px;
    color: var(--ink-soft);
    font-weight: 700;
    font-size: 15px;
    letter-spacing: 2px;
  }
</style>
</head>
<body>
  <main class="cover">
    <div class="cover-art" role="img" aria-label="Abstract background: shattered glass pane over flowing green, teal and blue light waves, with a dark opening at the centre"></div>

    <p class="spine-title">The Liminal Remainder</p>
    <p class="spine-issue">Vol. 1, No. 1, 2014</p>

    <h1 class="front-title">
      <span>THE</span>
      <span>LIMINAL</span>
      <span>REMAINDER</span>
    </h1>

    <p class="front-subtitle">
      <span>A Journal of Deconstruction</span>
      <span>and Psychoanalysis</span>
    </p>

    <p class="front-issue">Volume 1, Issue 1, 2014</p>
  </main>
</body>
</html>
```